Flyer-Design für Call Center
Zielgruppe
Lark Dialog ist ein Call Center und wir vertreiben die Fachliteratur von großen deutschen Verlagen (z.B. Brosen oder Wallmut). Unsere Telefonisten rufen in Krankenhäusern, Pflegeeinrichtungen, Kindergärten, Schulen an und bieten den leitenden Personen dort die für ihr Berufsfeld passende Fachliteratur zum kostenfreien Kennenlernen an.
Aufgrund der zahlreichen anstehenden Aufträge brauchen wir dringend neuen Teamzuwachs, insbesondere möchten wir Heidelberger Werkstudenten auf uns aufmerksam machen. Die Flyer sollen bei Erstsemesterparties oder vor den Universitätsmensen verteilt werden und die Studis ansprechen.
Ziel: Ganz viele Studenten bewerben sich um eine Stelle als Vertriebler bei Lark Dialog.
Aufgabenstellung
Den Inhalt für Vorder- und Rückseite habe ich bereits zusammengefasst, kann aber auch gekürzt / verlängert werden wenn das optisch besser wäre. (siehe pdf Dokument im Anhang)
Ich habe unseren bisherigen Flyer hinzugefügt wobei uns der nicht mehr besonders gut gefällt. Es wäre schön, ein paar junge Gesichter mit denen sich die Studenten identifizieren können auf dem Flyer zu haben. Aber lieber nicht das klassische Call Center Bild 'Hübsche lächelnde Dame mit Headset' ;-)
Schön wäre es auch visuell unseren größten Vorteil der 100% freien Arbeitszeiteinteilung hervorzuheben.

```html
<!DOCTYPE html>
<html lang="de">
<head>
<meta charset="utf-8">
<title>Lark Dialog – Werkstudent gesucht</title>
<link rel="stylesheet" href="https://fonts.googleapis.com/css2?family=Abel&family=Montserrat:wght@400;600;700&family=Open+Sans:wght@400;600&display=swap">
<style>
  :root{
    --bg:#8c8f93;
    --ink:#2b2c2f;
    --dark:#2f3033;
    --blue:#1fa3e6;
    --blue-deep:#1b6fb8;
    --light:#f2f3f4;
    --white:#ffffff;
    --grey-text:#cfd2d6;
  }
  *{box-sizing:border-box;margin:0;padding:0}
  html,body{width:1200px;height:675px;overflow:hidden;background:var(--bg)}
  .stage{position:relative;width:1200px;height:675px;display:flex;justify-content:center;align-items:center;gap:60px}
  .flyer{position:relative;width:290px;height:614px;overflow:hidden;box-shadow:0 8px 24px rgba(0,0,0,.35)}
  .flyer svg.shapes{position:absolute;inset:0}

  /* front */
  .front .headline{position:absolute;top:26px;left:0;right:0;text-align:center;font-family:"Abel",sans-serif}
  .front .headline .claim{font-size:31px;color:var(--ink);letter-spacing:.5px;line-height:1}
  .front .headline .role{font-size:20px;color:var(--blue-deep);letter-spacing:1.5px;margin-top:2px}
  .front .brand{position:absolute;top:392px;left:0;right:0;text-align:center;font-family:"Montserrat",sans-serif;font-weight:600;font-size:25px;letter-spacing:4px;color:var(--blue)}
  .front .web{position:absolute;top:430px;left:0;right:0;text-align:center;font-family:"Abel",sans-serif;font-size:17px;letter-spacing:2.5px;color:var(--white)}
  .front .contact{position:absolute;top:468px;left:0;right:0;text-align:center;font-family:"Abel",sans-serif;font-size:13.5px;line-height:1.3;color:var(--white)}
  .front .hours{position:absolute;top:548px;left:0;right:0;text-align:center;font-family:"Abel",sans-serif;font-size:12.5px;line-height:1.35;color:var(--white)}
  .front .hours .label{text-decoration:underline}

  /* back */
  .back{background:var(--dark)}
  .back .content{position:absolute;top:20px;left:18px;right:18px;font-family:"Open Sans",sans-serif;color:var(--grey-text);font-size:7.6px;line-height:1.45;text-align:center}
  .back h3{font-family:"Montserrat",sans-serif;font-weight:700;font-size:8.2px;color:var(--blue);text-transform:uppercase;letter-spacing:.3px;margin:10px 0 4px;line-height:1.3}
  .back h3:first-child{margin-top:0}
  .back p{margin-bottom:2px}
  .back ul{list-style:none;text-align:left;margin:4px 0 0 8px}
  .back li{display:flex;gap:6px;align-items:flex-start;margin-bottom:4px}
  .back li svg{flex:0 0 9px;margin-top:1px}
  .back .cta{position:absolute;bottom:18px;left:0;right:0;text-align:center;font-family:"Montserrat",sans-serif;color:var(--ink)}
  .back .cta .q{font-weight:700;font-size:12.5px;letter-spacing:.3px}
  .back .cta .sub{font-weight:700;font-size:8.4px;line-height:1.35;margin-top:3px}
  .back .cta .url{font-family:"Abel",sans-serif;font-size:17px;letter-spacing:2px;color:var(--blue-deep);margin-top:8px;padding-top:5px;border-top:1px solid var(--blue);display:inline-block}
</style>
</head>
<body>
<main class="stage">

  <section class="flyer front" aria-label="Vorderseite">
    <svg class="shapes" width="290" height="614" viewBox="0 0 290 614">
      <defs>
        <linearGradient id="paperLight" x1="0" y1="0" x2="1" y2="1">
          <stop offset="0" stop-color="#ffffff"/>
          <stop offset=".6" stop-color="#e9eaec"/>
          <stop offset="1" stop-color="#c9cbce"/>
        </linearGradient>
        <linearGradient id="photoTone" x1="0" y1="0" x2="1" y2="1">
          <stop offset="0" stop-color="#d9dadd"/>
          <stop offset=".5" stop-color="#b9a6a6"/>
          <stop offset="1" stop-color="#7f4d72"/>
        </linearGradient>
      </defs>
      <rect width="290" height="614" fill="url(#paperLight)"/>
      <path d="M0 345 Q140 420 290 300 L290 614 L0 614 Z" fill="var(--blue)"/>
      <path d="M0 356 Q140 430 290 314 L290 614 L0 614 Z" fill="var(--dark)"/>
      <path d="M92 118 A96 96 0 0 0 140 318 A104 104 0 0 1 92 118 Z" fill="var(--blue)"/>
      <circle cx="176" cy="214" r="96" fill="var(--dark)"/>
      <circle cx="176" cy="214" r="86" fill="url(#photoTone)" role="img" aria-label="Foto: zwei lächelnde Studierende mit Büchern und Ordnern"/>
    </svg>
    <div class="headline">
      <div class="claim">"YOU ARE WANTED!"</div>
      <div class="role">WERKSTUDENT GESUCHT</div>
    </div>
    <div class="brand">LARK DIALOG</div>
    <div class="web">WWW.LARKDIALOG-JOBS.DE</div>
    <div class="contact">Lindenhof-Allee 12<br>69115 Heidelberg<br>Tel. 06221 / 58 21 0<br>job@larkdialog.de</div>
    <div class="hours"><span class="label">ÖFFNUNGSZEITEN:</span><br>Mo - Do 8:00 - 16:00 &amp; Fr 8:00 - 15:00</div>
  </section>

  <section class="flyer back" aria-label="Rückseite">
    <svg class="shapes" width="290" height="614" viewBox="0 0 290 614">
      <path d="M0 505 Q170 500 290 440 L290 614 L0 614 Z" fill="var(--blue)"/>
      <path d="M0 514 Q170 510 290 452 L290 614 L0 614 Z" fill="var(--light)"/>
    </svg>
    <div class="content">
      <h3>Freie Zeiteinteilung, abwechslungsreiche Aufgaben &amp; ein lockeres Arbeitsklima</h3>
      <p>Du befindest Dich im Studium oder hast andere Verpflichtungen, möchtest aber trotzdem langfristig Dein Girokonto aufstocken und am liebsten Deine Arbeitszeiten komplett selbst bestimmen?</p>
      <h3>Dann bist Du bei uns genau richtig!</h3>
      <p>Lark Dialog sucht Verstärkung (m/w) für das Team am Standort Heidelberg. Wir zählen zu den führenden Dienstleistungsunternehmen für Verlagsmarketing in Deutschland und planen erfolgreiche Telefonmarketing Kampagnen für bekannte deutsche Verlage wie z.B. die Brosen Gruppe. Im Zuge dieser Kampagnen führen wir Gespräche mit interessierten Entscheidungsträgern aus Schulen, Kindertageseinrichtungen und Krankenhäusern und bieten Lösungen für die jeweiligen beruflichen Schwerpunkte in Form hochwertiger Fachliteratur an.</p>
      <h3>Du bist genau die/der Richtige, wenn Du …</h3>
      <ul>
        <li><svg width="9" height="9" viewBox="0 0 9 9"><rect width="9" height="9" fill="#8a8d91"/><path d="M2 4.6 L3.8 6.4 L7.2 2.4" stroke="#2f3033" stroke-width="1.4" fill="none"/></svg>über eine sehr gute Ausdrucksweise verfügst</li>
        <li><svg width="9" height="9" viewBox="0 0 9 9"><rect width="9" height="9" fill="#8a8d91"/><path d="M2 4.6 L3.8 6.4 L7.2 2.4" stroke="#2f3033" stroke-width="1.4" fill="none"/></svg>viel Spaß am Kundenkontakt hast</li>
        <li><svg width="9" height="9" viewBox="0 0 9 9"><rect width="9" height="9" fill="#8a8d91"/><path d="M2 4.6 L3.8 6.4 L7.2 2.4" stroke="#2f3033" stroke-width="1.4" fill="none"/></svg>eine hohe Eigenmotivation, Kommunikationsstärke und Fingerspitzengefühl mitbringst</li>
      </ul>
      <h3>Wir bieten Dir …</h3>
      <ul>
        <li><svg width="9" height="9" viewBox="0 0 9 9"><rect width="9" height="9" fill="#8a8d91"/><path d="M2 4.6 L3.8 6.4 L7.2 2.4" stroke="#2f3033" stroke-width="1.4" fill="none"/></svg>freier Zeiteinteilung (8 - 20 Std./Woche je nach Wunsch und zu selbst bestimmten Zeiten)</li>
        <li><svg width="9" height="9" viewBox="0 0 9 9"><rect width="9" height="9" fill="#8a8d91"/><path d="M2 4.6 L3.8 6.4 L7.2 2.4" stroke="#2f3033" stroke-width="1.4" fill="none"/></svg>einen unbefristeten Arbeitsvertrag</li>
        <li><svg width="9" height="9" viewBox="0 0 9 9"><rect width="9" height="9" fill="#8a8d91"/><path d="M2 4.6 L3.8 6.4 L7.2 2.4" stroke="#2f3033" stroke-width="1.4" fill="none"/></svg>eine intensive Begleitung in der Einarbeitungsphase</li>
        <li><svg width="9" height="9" viewBox="0 0 9 9"><rect width="9" height="9" fill="#8a8d91"/><path d="M2 4.6 L3.8 6.4 L7.2 2.4" stroke="#2f3033" stroke-width="1.4" fill="none"/></svg>ein ziemlich cooles Team und Spaß bei der Arbeit</li>
        <li><svg width="9" height="9" viewBox="0 0 9 9"><rect width="9" height="9" fill="#8a8d91"/><path d="M2 4.6 L3.8 6.4 L7.2 2.4" stroke="#2f3033" stroke-width="1.4" fill="none"/></svg>ein Festgehalt von 10,00€/Std.</li>
      </ul>
    </div>
    <div class="cta">
      <div class="q">INTERESSE GEWECKT?</div>
      <div class="sub">DANN BEWIRB' DICH IN NUR ZWEI MINUTEN<br>ÜBER UNSER ONLINE BEWERBUNGSPORTAL:</div>
      <div class="url">WWW.LARKDIALOG-JOBS.DE</div>
    </div>
  </section>

</main>
</body>
</html>
```